Wordpress Design Project (Halvern)

We need a wordpress design for an established auction and real estate company based in Virginia. The winning design will incorporate the colors of logo (red and black) creatively with an accent color in a very professional and clean layout.

Industry/Entity Type

Real Estate

Requirements
Must have
• We will require winning designer to provide a layered PSD (Adobe photoshop) concept file, along with any non-standard font files used.

Horizontal Navigation menu with these links:
Home - Upcoming Auctions - Past Auctions - For Sale- Consignments - About Us - Highlights - Contact Us

A slideshow element on the home page using the placeholder image provided.

Sidebar widgets to be included are: Email sign-up form - Featured Auctions - Featured Assets for Sale (see attached for visual of these widgets)

attached logos in footer with company contact info

```html
<!DOCTYPE html>
<html lang="en">
<head>
<meta charset="utf-8">
<title>Halvern Enterprises</title>
<link href="https://fonts.googleapis.com/css2?family=Bebas+Neue&family=Pathway+Gothic+One&display=swap" rel="stylesheet">
<style>
:root{
  --red:#e8161b;
  --red-deep:#b50c10;
  --red-bright:#ff1e1e;
  --ink:#231616;
  --nav:#2a2a2a;
  --panel:#353535;
  --panel-light:#474747;
  --white:#ffffff;
  --text:#555555;
  --footer:#ececec;
  --footer-text:#a9a9a9;
  --sky:#a9c3de;
  --grass:#5f7f3a;
}
*{box-sizing:border-box;margin:0;padding:0}
html,body{width:1121px;height:1200px;overflow:hidden}
body{
  position:relative;
  background:radial-gradient(ellipse at 50% 30%,var(--red-bright) 0%,var(--red) 40%,var(--red-deep) 100%);
  font-family:"Pathway Gothic One",sans-serif;
}
.brand-tab{
  position:absolute;left:435px;top:0;width:249px;height:88px;
  background:var(--white);
  clip-path:polygon(0 0,100% 0,100% 72%,50% 100%,0 72%);
  display:flex;align-items:center;justify-content:center;gap:8px;padding-bottom:22px;
}
.brand-mark{width:22px;height:22px;background:var(--red)}
.brand-name{font-family:"Bebas Neue",sans-serif;font-size:34px;color:var(--ink);letter-spacing:1px;line-height:1}
.site{position:absolute;left:93px;top:98px;width:935px}
.main-nav{
  height:41px;background:linear-gradient(#333,#1e1e1e);border-radius:4px 4px 0 0;
  display:flex;align-items:center;padding-left:28px;
}
.main-nav a{
  font-family:"Bebas Neue",sans-serif;font-size:17px;color:var(--white);text-decoration:none;
  position:relative;height:41px;line-height:43px;
}
.main-nav a.is-current{color:var(--red)}
.main-nav a.is-current::after{
  content:"";position:absolute;left:50%;bottom:0;transform:translateX(-50%);
  border:6px solid transparent;border-bottom-color:var(--red);border-top:0;
}
.slider{position:relative;height:449px;overflow:hidden}
.slide-photo{
  position:absolute;inset:0;
  background:linear-gradient(180deg,var(--sky) 0%,#c9d6e2 30%,#8c7865 45%,#7c6a58 70%,var(--grass) 82%,#4c6a2e 100%);
}
.slide-caption{
  position:absolute;left:560px;top:112px;width:311px;height:139px;
  background:rgba(20,20,20,.88);padding:18px 12px 0 14px;
  font-family:"Bebas Neue",sans-serif;font-size:30px;line-height:37px;color:var(--white);
}
.slide-caption em{font-style:normal;color:var(--red)}
.slide-dots{position:absolute;left:733px;top:278px;display:flex;gap:6px}
.slide-dots span{width:13px;height:13px;border-radius:50%;background:var(--red)}
.slider-arrow{
  position:absolute;top:336px;width:32px;height:33px;background:var(--white);
  display:flex;align-items:center;justify-content:center;z-index:2;
}
.slider-arrow.prev{left:82px}
.slider-arrow.next{left:1010px}
.widgets{
  height:199px;display:flex;
  background:linear-gradient(180deg,var(--panel) 0%,var(--panel-light) 55%,#2e2e2e 100%);
  border-radius:0 0 4px 4px;
}
.widget{padding:24px 20px 0 20px;color:var(--white)}
.widget + .widget{border-left:2px solid #2a2a2a}
.widget-title{font-family:"Bebas Neue",sans-serif;font-size:22px;font-weight:400;color:var(--white);margin-bottom:8px}
.widget-title em{font-style:normal;color:var(--red)}
.newsletter{width:318px}
.newsletter p{font-size:16px;line-height:18px;color:#dcdcdc}
.email-field{
  margin-top:4px;width:277px;height:31px;background:var(--white);border:1px solid #bbb;border-radius:3px;
  font-family:Arial,sans-serif;font-size:10px;color:#444;padding:9px 6px;
}
.subscribe{
  margin-top:9px;width:99px;height:33px;background:linear-gradient(#fafafa,#cfcfcf);border-radius:2px;
  font-family:"Bebas Neue",sans-serif;font-size:21px;color:#333;text-align:center;line-height:35px;
}
.featured-auctions{width:317px;padding-left:15px}
.featured-assets{width:300px;padding-left:17px}
.feature-item{display:flex;gap:4px;margin-top:20px}
.feature-photo{
  flex:none;width:100px;height:66px;
  background:linear-gradient(180deg,#9fbbd8 0%,#c2b29d 40%,#8d7a66 65%,#5b7b35 100%);
}
.feature-body{font-size:15px;line-height:21px;color:#e6e6e6}
.feature-body b{font-weight:400;color:var(--red)}
.asset-body{font-size:13px;line-height:16px;color:#e6e6e6}
.asset-body a{display:block;font-size:16px;color:var(--red);text-decoration:none;margin-bottom:2px}
.home-values{background:var(--white);height:214px;padding:10px 10px 0 10px;border-bottom:1px solid var(--red)}
.section-title{font-family:"Bebas Neue",sans-serif;font-size:22px;font-weight:400;color:var(--red)}
.home-values .content{display:flex;gap:14px;margin-top:8px}
.values-photo{
  flex:none;width:146px;height:99px;margin-left:2px;
  background:linear-gradient(180deg,#8fb2db 0%,#b9ccdf 35%,#a4917b 55%,#6d8b45 85%,#8a8a80 100%);
}
.home-values p{font-size:16.4px;line-height:22.4px;color:var(--text);text-align:justify;width:743px}
.site-footer{
  height:199px;background:var(--footer);display:flex;
}
.footer-links{width:479px;padding:36px 0 0 17px;display:flex;position:relative}
.footer-links::after{content:"";position:absolute;right:0;top:0;width:3px;height:100%;background:#dcdcdc}
.footer-heading{font-family:"Bebas Neue",sans-serif;font-size:18px;font-weight:400;color:var(--red);margin-bottom:8px}
.quicklinks{width:297px}
.quicklinks ul{list-style:none;columns:2;column-gap:0;width:290px}
.quicklinks li{font-family:"Bebas Neue",sans-serif;font-size:14px;color:var(--footer-text);line-height:22.4px;padding-left:3px}
.social-icons{display:flex;gap:6px;margin-top:16px}
.social-icons span{width:27px;height:27px;border-radius:50%;border:2px solid #bdbdbd}
.footer-contact{padding:46px 0 0 44px}
.partner-badges{display:flex;gap:8px;align-items:center;height:54px}
.partner-badges span{background:#c9c9c9;height:34px}
.company-name{font-family:"Bebas Neue",sans-serif;font-size:18px;font-weight:400;color:var(--red);margin-top:10px}
.company-address{font-family:"Bebas Neue",sans-serif;font-size:14px;color:var(--footer-text);margin-top:2px}
</style>
</head>
<body>
  <header class="brand-tab">
    <span class="brand-mark"></span>
    <span class="brand-name">Halvern Enterprises</span>
  </header>

  <div class="slider-arrow prev"><svg width="12" height="14" viewBox="0 0 12 14"><path d="M9 1 3 7l6 6" fill="none" stroke="#111" stroke-width="3"/></svg></div>
  <div class="slider-arrow next"><svg width="12" height="14" viewBox="0 0 12 14"><path d="M3 1l6 6-6 6" fill="none" stroke="#111" stroke-width="3"/></svg></div>

  <div class="site">
    <nav class="main-nav">
      <a class="is-current" style="margin-right:57px">Home</a>
      <a style="margin-right:54px">Upcoming Auctions</a>
      <a style="margin-right:54px">Past Auctions</a>
      <a style="margin-right:54px">For Sale</a>
      <a style="margin-right:54px">Consignments</a>
      <a style="margin-right:56px">About Us</a>
      <a style="margin-right:54px">Highlights</a>
      <a>Contact Us</a>
    </nav>

    <section class="slider">
      <div class="slide-photo" role="img" aria-label="Two-storey brick and siding family house with front porch, garage and lawn under a blue sky"></div>
      <div class="slide-caption"><em>Thinking of selling your home</em>, or just curious to see what your home is worth?</div>
      <div class="slide-dots"><span></span><span></span><span></span><span></span></div>
    </section>

    <section class="widgets">
      <div class="widget newsletter">
        <h2 class="widget-title"><em>Newsletter</em> Signup</h2>
        <p>Stay on top of all things real estate with our free weekly newsletter.</p>
        <div class="email-field">Enter your Email - ID</div>
        <div class="subscribe">Subscribe</div>
      </div>
      <div class="widget featured-auctions">
        <h2 class="widget-title"><em>Featured</em> Auctions</h2>
        <div class="feature-item">
          <div class="feature-photo" role="img" aria-label="Suburban house offered at auction"></div>
          <div class="feature-body">Dream House Auction<br><b>Start Time :</b> Wed, April 10, 2013<br><b>Location :</b> 1187 Linden Hollow, VA 24012</div>
        </div>
      </div>
      <div class="widget featured-assets">
        <h2 class="widget-title"><em>Featured Assets</em> For Sale</h2>
        <div class="feature-item">
          <div class="feature-photo" role="img" aria-label="Family house listed for sale"></div>
          <div class="asset-body"><a>Just casually browse homes</a>Thinking of selling your home, or just curious to see what your home is worth?</div>
        </div>
      </div>
    </section>

    <section class="home-values">
      <h2 class="section-title">Check out home values</h2>
      <div class="content">
        <div class="values-photo" role="img" aria-label="Family house with porch and driveway"></div>
        <p>Thinking of selling your home, or just curious to see what your home is worth? Use our handy home valuation estimator to check the value of your current home. You can also get a Comparable Market Assessment (CMA) from a local market expert, taking into consideration unique characteristics, home improvements and other home, neighborhood and area information not always available in the public record.Research Schools and Local Communities Schools are one of the important factors in deciding where to buy your next home. One of the most important factors in choosing a home is picking the right neighborhood. Check out school ratings and get the</p>
      </div>
    </section>

    <footer class="site-footer">
      <div class="footer-links">
        <div class="quicklinks">
          <h3 class="footer-heading">Quicklinks</h3>
          <ul>
            <li>Home</li><li>Upcoming Auctions</li><li>Past Auctions</li><li>For Sale</li><li>Consignments</li>
            <li>About Us</li><li>Highlights</li><li>Contact Us</li>
          </ul>
        </div>
        <div class="follow">
          <h3 class="footer-heading">Follow Us</h3>
          <div class="social-icons"><span></span><span></span><span></span></div>
        </div>
      </div>
      <div class="footer-contact">
        <div class="partner-badges">
          <span style="width:34px"></span>
          <span style="width:68px"></span>
          <span style="width:70px"></span>
          <span style="width:50px;height:50px;border-radius:50%"></span>
          <span style="width:104px;height:40px"></span>
        </div>
        <h3 class="company-name">Halvern Enterprises</h3>
        <p class="company-address">410 Alder Crest Rd. Suite 200, - Charlottesville, VA 22903 - Phone: 434-555-0182</p>
      </div>
    </footer>
  </div>
</body>
</html>
```